Web Design Project

I have a website which looks dull and uninteresting. I'd like to apply a fresh and clean look to it, which better reflects the quality of the service I sell.The website address is http://www.brightquillpages.co.uk.

Target Market(s)

Financial advisers (financially sophisticated individuals)

Industry/Entity Type

It Service

Requirements
Should not have
• Please do not use obvious but irrelevant and boring imagery such as banks, pages from the DL, money, books or libraries. Prefer slick relevant graphics and crisp typography.

```html
<!DOCTYPE html>
<html lang="en">
<head>
<meta charset="utf-8">
<title>BrightQuillPages.co.uk</title>
<link href="https://fonts.googleapis.com/css2?family=Arimo:wght@400;700&family=Open+Sans:wght@400;600&display=swap" rel="stylesheet">
<style>
:root{
  --page:#ececec;
  --panel:#f7f7f7;
  --panel-grey:#cfcfcf;
  --border:#d6d6d6;
  --dark:#2f2f2f;
  --tab:#555555;
  --text:#333333;
  --muted:#666666;
  --red:#d8241c;
  --footer:#6b6b6b;
  --white:#ffffff;
}
*{box-sizing:border-box;margin:0;padding:0}
html,body{width:853px;height:1200px;overflow:hidden}
body{position:relative;background:var(--page);font-family:"Arimo",Arial,sans-serif;color:var(--text)}
.abs{position:absolute}
.top-rule{left:0;top:0;width:853px;height:3px;background:var(--dark)}
.top-rule::before,.top-rule::after{content:"";position:absolute;top:0;height:3px;width:100px;background:var(--red)}
.top-rule::before{left:0}.top-rule::after{right:0}

.brand{left:18px;top:24px}
.brand-name{font-family:"Open Sans",sans-serif;font-size:25px;color:var(--dark);letter-spacing:-.3px;line-height:30px}
.brand-tag{font-family:"Open Sans",sans-serif;font-size:12px;color:var(--dark);margin-left:62px;line-height:14px}

.search{left:657px;top:17px;width:188px;height:20px;background:var(--dark);color:#ddd;font-size:12px;padding:3px 4px}
.search svg{position:absolute;right:5px;top:2px}
.social{left:708px;top:47px;display:flex;gap:5px}
.social span{width:30px;height:30px;border-radius:5px;background:#8a9097}

.panel{background:var(--panel);border:1px solid var(--border);border-radius:8px}
.nav{left:8px;top:90px;width:226px;height:308px}
.nav-home{left:3px;top:104px;width:114px;height:26px;background:var(--tab);color:#fff;font-family:"Open Sans",sans-serif;font-size:13px;padding:5px 0 0 24px;clip-path:polygon(0 0,100px 0,114px 13px,100px 26px,0 26px)}
.nav-list{left:26px;top:135px;list-style:none;font-family:"Open Sans",sans-serif;font-size:13px;color:#444}
.nav-list li{height:35.5px;line-height:20px;padding-top:7px;width:138px;border-top:2px dashed #d0d0d0}

.slider{left:173px;top:120px;width:674px;height:254px;background:#fff;border-radius:8px;box-shadow:0 1px 4px rgba(0,0,0,.35)}
.slide{left:180px;top:127px;width:660px;height:240px;border-radius:6px;background:linear-gradient(120deg,#2a2f38,#4c5461 45%,#1b1e25)}
.slide-cap{left:193px;top:310px;color:#fff;font-family:"Open Sans",sans-serif;font-size:17px;line-height:22px}
.pager{left:459px;top:384px;width:101px;height:19px;border-radius:10px;background:#ddd;border:1px solid #999;font-size:10px;color:#777;display:flex;align-items:center;justify-content:space-between;padding:0 2px}
.pager b{width:14px;height:14px;border-radius:50%;background:#444;color:#fff;font-size:9px;line-height:14px;text-align:center}

.links{left:8px;top:406px;width:226px;height:273px;padding:12px 0 0 17px;list-style:none;font-family:"Open Sans",sans-serif;font-size:10px;color:#222}
.links li{height:17.7px}
.links li:first-child{font-weight:600}

.content{left:241px;top:425px;width:605px;height:440px;padding:12px 16px}
.content h1{font-size:13.4px;line-height:22px;color:#222;font-weight:700}
.content p{font-size:10.4px;line-height:23px;color:var(--muted);margin-top:6px}
.content p+p{margin-top:21px}
.price{left:262px;top:810px;width:564px;height:40px;background:#d4d4d4;padding:3px 16px}
.price strong{display:block;font-size:16px;line-height:20px;color:#222;white-space:nowrap}
.price a{display:block;color:var(--red);font-size:10.5px;line-height:14px;text-decoration:none}

.box-grey{background:var(--panel-grey);border-radius:8px}
.latest{width:226px;height:175px}
.latest-head{position:absolute;left:7px;top:23px;width:219px;height:19px;background:var(--dark);color:#fff;font-weight:700;font-size:13px;padding:2px 0 0 36px}
.latest-head i{position:absolute;left:-2px;top:-8px;width:32px;height:32px;border-radius:50%;background:#eee;border:2px solid #555}
.latest ol{position:absolute;left:8px;top:49px;list-style:none;font-size:10.5px;line-height:12px;color:#222}
.latest li{display:flex;align-items:center;height:32px;width:216px;border-bottom:1px solid #eee}
.latest li span{flex:0 0 24px;height:24px;border-radius:50%;background:#fff;border:2px solid #777;text-align:center;font-size:11px;line-height:20px;margin-right:11px}
.latest .more{position:absolute;right:9px;bottom:5px;font-size:9px;color:#222}

.guides{left:245px;top:876px;width:361px;height:175px;padding:6px 14px 6px 10px;font-size:10px;line-height:12px;color:#222}
.guides a{color:var(--red);text-decoration:none}
.guide{position:absolute;top:62px;width:84px;font-size:8px;line-height:10px}
.guide div{width:83px;height:73px;background:linear-gradient(#e8e2d8,#a6997f);margin-bottom:6px}

.login{left:618px;top:876px;width:228px;height:175px;font-size:11px}
.login h2{position:absolute;left:0;top:14px;width:228px;height:21px;background:var(--dark);color:#fff;font-size:13px;text-align:center;line-height:21px}
.login label{position:absolute;left:7px}
.login .field{position:absolute;left:65px;width:157px;height:18px;background:#fff;border:1px solid #aaa}
.login .btn{position:absolute;left:165px;top:117px;width:52px;height:17px;background:var(--red);color:#fff;border-radius:3px;text-align:center;line-height:17px}
.login .remember{position:absolute;left:70px;top:138px;color:#555}
.login .remember i{display:inline-block;width:10px;height:10px;background:#fff;border:1px solid #999;margin-right:4px;vertical-align:-1px}

.footer{left:0;top:1065px;width:853px;height:135px;background:var(--footer);color:#fff;font-size:11px;text-align:center}
.footer p:first-child{margin-top:26px}
.footer p+p{margin-top:17px}
</style>
</head>
<body>
<div class="abs top-rule"></div>

<header class="abs brand">
  <div class="brand-name">BrightQuillPages.co.uk</div>
  <div class="brand-tag">Words to use as you please</div>
</header>

<div class="abs search">Search
  <svg width="16" height="16" viewBox="0 0 16 16"><circle cx="8" cy="8" r="7" fill="#ddd"/><circle cx="7" cy="7" r="3" fill="none" stroke="#555" stroke-width="1.5"/><line x1="9" y1="9" x2="12" y2="12" stroke="#555" stroke-width="1.5"/></svg>
</div>
<div class="abs social"><span></span><span></span><span></span><span></span></div>

<nav class="abs panel nav"></nav>
<div class="abs nav-home">Home</div>
<ul class="abs nav-list">
  <li>A - Z Articles</li><li>Inheritance Tax</li><li>Insurances</li><li>Mortgages</li><li>Other</li><li>Retirement</li><li>Saving and Investment</li>
</ul>

<div class="abs slider"></div>
<div class="abs slide" role="img" aria-label="Rolled banknotes on a dark background"></div>
<p class="abs slide-cap">Lorem Ipsum is simply dummy text of the<br>printing and typesetting industry.</p>
<div class="abs pager"><b>&lsaquo;</b>1 2 3 4 5<b>&rsaquo;</b></div>

<ul class="abs panel links">
  <li>Home</li><li>Samples</li><li>The people who write the articles</li><li>Please don't lift our words</li><li>A - Z of articles</li><li>Enter the library</li><li>Join the library here</li><li>Some FAQs</li><li>Contact us</li><li>A few terms &amp; conditions</li><li>Forgotten your password?</li><li>A comment to make?</li><li>A question to ask?</li><li>Want something writing?</li>
</ul>

<main class="abs panel content">
  <h1>131 ready-written, copyright-free personal financial planning articles which you can use or adapt in almost any way you want and for as long as you want.</h1>
  <p>Our articles provide succinct, clear and up to date explanations about financial products and aspects of financial planning for you to use on your website, in e-mails, marketing literature and newsletters (but not in editorial contributions please).</p>
  <p>We summarise the important ins and outs out products: from the very simplest (life insurance, savings accounts and unit trusts for example) to the most complex of topics such as Behavioural Finance, structured products and Venture Capital Trusts. Where the subject is particularly lengthy — pensions and IHT planning for example — it's divided into component parts. You can then use those component parts as building blocks for the production of your own guides.<br>None of the articles are biased towards any product provider, nor do they contain advice, money-saving tips, 'best buys' or special offers. There's a bare minimum of jargon and each article is structured correctly and free of ambiguity.</p>
  <p>Articles are updated as and when necessary and new articles and guides are added free of charge whenever we find a subject that should be added or we're asked to write an article by a member.</p>
  <p>To view our library, follow this link. To see samples of the articles go here.</p>
</main>
<div class="abs price"><strong>£49 a year, at least 131 articles (plus free guides as they're published)</strong><a>follow this link to have full access to the library.</a></div>

<section class="abs box-grey latest" style="left:8px;top:689px">
  <div class="latest-head"><i></i>Articles added in June 2011:</div>
  <ol>
    <li><span>1</span>Fundamental Analysis and Key Ratios</li>
    <li><span>2</span>Inheritance Tax Planning and Equity Release</li>
    <li><span>3</span>Inheritance Tax Planning and Qualifying</li>
  </ol>
  <div class="more">read more...</div>
</section>

<section class="abs box-grey latest" style="left:8px;top:876px">
  <div class="latest-head"><i></i>Articles added in July 2011:</div>
  <ol>
    <li><span>1</span>Fundamental Analysis and Key Ratios</li>
    <li><span>2</span>Inheritance Tax Planning and Equity Release</li>
    <li><span>3</span>Inheritance Tax Planning and Qualifying</li>
  </ol>
  <div class="more">read more...</div>
</section>

<section class="abs box-grey guides">
  <p><strong>CHECK OUT MY TWO FREE GUIDES</strong> There are still many people who either have no idea or the wrong idea about financial advice and financial advisers. That's why I've written two guides which you can use free of charge once you become a member -- <a>here are some more details...</a></p>
  <div class="guide" style="left:15px"><div role="img" aria-label="Hand holding out banknotes"></div>Why financial advice can never be free</div>
  <div class="guide" style="left:142px"><div role="img" aria-label="Hands counting money"></div>What it takes to be financial adviser</div>
  <div class="guide" style="left:264px"><div role="img" aria-label="Figure beside a large currency symbol" style="background:linear-gradient(#c9c3d8,#6a6f8a)"></div>IHT planning a guessing and waiting game</div>
</section>

<section class="abs box-grey login">
  <h2>Members Login</h2>
  <label style="top:58px">Email:</label><div class="field" style="top:55px"></div>
  <label style="top:93px">Password:</label><div class="field" style="top:89px"></div>
  <div class="btn">Log in</div>
  <div class="remember"><i></i>Remember me?</div>
</section>

<footer class="abs footer">
  <p>Copyrights © 2011 www.brightquillpages.co.uk. All rights reserved</p>
  <p>Terms and conditions | Privacy Policy</p>
</footer>
</body>
</html>
```